Tulvo Website

I have recently launched a gay social networking application called
Tulvo. It's available in the US, UK and Australian Orvane App Stores. I need a website to promote the application, promote it's features and house terms and conditions and contact details.

The current basic quill deck page is www.tulvoapp.example

I have attached screen designs for the app.

Competitors include:

www.brakko.example
www.plindt.example
www.getvarlux.example
Updates

Hi All. I have committed the payment. The designs I've seen so far are too simple, I want something more edgy with less white space on the screen. Thanks.

Hi Everyone. Thank you for your deigns. There are some great designs here. I'm in the process of selection and will choose one shortly. I really appreciate everyone's time and effort!!

Marcus

Target Market(s)

Gay men aged 18 to 60

Industry/Entity Type

House

Font styles to use
Sans Serif

Requirements
Must have
• About Page
Terms and Conditions Page
Privacy Policy Page
Link to Orvane Store
Features Page

```html
<!DOCTYPE html>
<html lang="en">
<head>
<meta charset="utf-8">
<title>Tulvo – True Faces, Fresh Shots, Today.</title>
<link rel="stylesheet" href="https://fonts.googleapis.com/css2?family=Open+Sans:wght@400;600;700;800&display=swap">
<style>
  :root {
    --red-dark: #8e0008;
    --red: #b5000d;
    --red-bright: #d3101a;
    --gold: #ffc21a;
    --white: #ffffff;
    --paper: #f2f2f2;
    --ink: #2a2a2a;
    --footer: #2c2c2c;
    --ring: #c9c9c9;
  }
  * { box-sizing: border-box; margin: 0; padding: 0; }
  html, body { width: 1200px; height: 1112px; overflow: hidden; }
  body { font-family: "Open Sans", Arial, sans-serif; color: var(--ink); background: var(--paper); position: relative; }

  .site-header {
    position: absolute; left: 0; top: 0; width: 1200px; height: 96px;
    background: linear-gradient(180deg, var(--red) 0%, var(--red-dark) 100%);
    border-bottom: 1px solid #6d0006;
    box-shadow: 0 2px 6px rgba(0,0,0,.35);
    z-index: 2;
  }
  .brand { position: absolute; left: 104px; top: 14px; color: var(--white); }
  .brand-name { font-size: 42px; font-weight: 800; line-height: 1; letter-spacing: -1px; }
  .brand-tagline { font-size: 12.5px; font-weight: 700; margin-top: 4px; }

  .follow { position: absolute; right: 100px; top: 19px; display: flex; align-items: center; gap: 8px; }
  .follow-label { font-size: 11px; color: #f0c6c8; margin-right: 4px; letter-spacing: .3px; }
  .social-dot { width: 19px; height: 19px; border-radius: 50%; background: var(--white); }

  .main-nav { position: absolute; right: 100px; top: 58px; display: flex; }
  .main-nav a { color: var(--white); text-decoration: none; font-size: 14px; font-weight: 700; padding: 0 12px; border-left: 1px solid rgba(255,255,255,.35); line-height: 1; }
  .main-nav a:first-child { border-left: 0; }
  .main-nav a:last-child { padding-right: 0; }
  .main-nav a.is-current { color: var(--gold); }

  .hero {
    position: absolute; left: 0; top: 96px; width: 1200px; height: 458px;
    background: radial-gradient(ellipse at 45% 40%, var(--red-bright) 0%, var(--red) 45%, var(--red-dark) 100%);
  }
  .hero-devices {
    position: absolute; left: 102px; top: 30px; width: 448px; height: 400px;
    border-radius: 34px;
    background: linear-gradient(160deg, #3a3a3a 0%, #141414 55%, #5a5a5a 100%);
    opacity: .92;
  }
  .hero-copy { position: absolute; left: 584px; top: 138px; width: 470px; color: var(--white); }
  .hero-title { font-size: 44px; font-weight: 600; line-height: 1; letter-spacing: -.3px; }
  .hero-text { font-size: 15.5px; line-height: 27.5px; margin-top: 17px; }
  .download-row { position: absolute; left: 587px; top: 296px; display: flex; gap: 22px; }
  .download-btn {
    width: 197px; height: 62px; border-radius: 3px;
    background: linear-gradient(180deg, #ffffff 0%, #e3e3e3 100%);
    box-shadow: 0 2px 4px rgba(0,0,0,.4);
    display: flex; align-items: center; padding-left: 28px; gap: 18px;
    color: var(--red-dark); font-size: 19.5px; font-weight: 600; text-decoration: none;
  }
  .store-dot { width: 30px; height: 30px; border-radius: 50%; background: var(--red-dark); }

  .section-title { font-size: 24px; font-weight: 700; color: var(--ink); letter-spacing: .2px; }
  .features { position: absolute; left: 103px; top: 570px; width: 1000px; }
  .feature-grid { position: relative; margin-top: 14px; height: 240px; }
  .feature { position: absolute; width: 330px; display: flex; gap: 14px; }
  .feature-thumb {
    width: 106px; height: 106px; border-radius: 50%; flex: none;
    border: 3px solid var(--ring);
    background: radial-gradient(circle at 45% 40%, #c99a83 0%, #7a5444 55%, #3a2a26 100%);
  }
  .feature-thumb.map { background: linear-gradient(135deg, #e9e4d6 0%, #cfd8c2 60%, #a9c6e3 100%); }
  .feature-thumb.chat { background: linear-gradient(180deg, #e8e8e8 0%, #cfcfcf 70%, #8b3a3a 100%); }
  .feature-name { font-size: 16px; font-weight: 700; margin-top: 10px; }
  .feature-text { font-size: 14.2px; line-height: 22px; margin-top: 2px; }

  .about { position: absolute; left: 103px; top: 870px; width: 1000px; }
  .about-text { font-size: 14px; line-height: 22.6px; margin-top: 6px; }

  .site-footer { position: absolute; left: 0; top: 1020px; width: 1200px; height: 92px; background: var(--footer); color: var(--white); }
  .footer-nav { position: absolute; left: 102px; top: 33px; display: flex; gap: 20px; }
  .footer-nav a { color: var(--white); font-size: 13px; text-decoration: none; }
  .copyright { position: absolute; left: 102px; top: 54px; font-size: 13px; }
  .footer-social { position: absolute; right: 100px; top: 30px; display: flex; gap: 9px; }
  .footer-social .social-dot { width: 31px; height: 31px; }
</style>
</head>
<body>
  <header class="site-header">
    <div class="brand">
      <div class="brand-name">Tulvo</div>
      <div class="brand-tagline">True Faces, Fresh Shots, Today.</div>
    </div>
    <div class="follow">
      <span class="follow-label">FOLLOW US</span>
      <span class="social-dot" role="img" aria-label="Social network link"></span>
      <span class="social-dot" role="img" aria-label="Social network link"></span>
      <span class="social-dot" role="img" aria-label="Social network link"></span>
      <span class="social-dot" role="img" aria-label="Video channel link"></span>
    </div>
    <nav class="main-nav">
      <a class="is-current" href="#">HOME</a>
      <a href="#">ABOUT US</a>
      <a href="#">ORVANE STORE</a>
      <a href="#">FEATURES</a>
      <a href="#">TERMS &amp; CONDITIONS</a>
      <a href="#">CONTACT US</a>
    </nav>
  </header>

  <section class="hero">
    <div class="hero-devices" role="img" aria-label="Three smartphones showing the Tulvo chat, nearby guys grid and profile screens"></div>
    <div class="hero-copy">
      <h1 class="hero-title">lorem Ipsum Doller</h1>
      <p class="hero-text">Tulvo enforces real pics. Users can't upload fake pics they have downloaded from other people's profiles or the internet, bringing some much welcomed authenticity to online dating.</p>
    </div>
    <div class="download-row">
      <a class="download-btn" href="#"><span class="store-dot"></span>Download</a>
      <a class="download-btn" href="#"><span class="store-dot"></span>Download</a>
    </div>
  </section>

  <section class="features">
    <h2 class="section-title">FEATURES</h2>
    <div class="feature-grid">
      <div class="feature" style="left:0;top:0">
        <div class="feature-thumb" role="img" aria-label="Profile photo screen with thumbnail strip"></div>
        <div><h3 class="feature-name">MULTIPLE PHOTOS</h3><p class="feature-text">Tulvo enforces real pics.<br>Users can't upload fake pics<br>they have downloaded.</p></div>
      </div>
      <div class="feature" style="left:366px;top:0">
        <div class="feature-thumb" role="img" aria-label="Private photo screen"></div>
        <div><h3 class="feature-name">PRIVATE PHOTOS</h3><p class="feature-text">Tulvo enforces real pics.<br>Users can't upload fake pics<br>they have downloaded.</p></div>
      </div>
      <div class="feature" style="left:697px;top:0">
        <div class="feature-thumb chat" role="img" aria-label="Chat conversation screen"></div>
        <div><h3 class="feature-name">CHAT</h3><p class="feature-text">Tulvo enforces real pics.<br>Users can't upload fake pics<br>they have downloaded.</p></div>
      </div>
      <div class="feature" style="left:0;top:120px">
        <div class="feature-thumb map" role="img" aria-label="Street map for exploring nearby users"></div>
        <div><h3 class="feature-name">EXPLORE</h3><p class="feature-text">Tulvo enforces real pics.<br>Users can't upload fake pics<br>they have downloaded.</p></div>
      </div>
      <div class="feature" style="left:366px;top:120px">
        <div class="feature-thumb" role="img" aria-label="Shared profile video screen"></div>
        <div><h3 class="feature-name">SHARE PROFILES</h3><p class="feature-text">Tulvo enforces real pics.<br>Users can't upload fake pics<br>they have downloaded.</p></div>
      </div>
      <div class="feature" style="left:697px;top:120px">
        <div class="feature-thumb" role="img" aria-label="Favourite profile screen"></div>
        <div><h3 class="feature-name">FAVORITES</h3><p class="feature-text">Tulvo enforces real pics.<br>Users can't upload fake pics<br>they have downloaded.</p></div>
      </div>
    </div>
  </section>

  <section class="about">
    <h2 class="section-title">ABOUT US</h2>
    <p class="about-text">Lorem Ipsum is simply dummy text of the printing and typesetting industry. Lorem Ipsum has been the industry's standard dummy text ever since the 1500s, when an unknown printer took a galley of type and scrambled it to make a type specimen book. It has survived not only five centuries, but also the leap into electronic typesetting, remaining essentially unchanged. It was popularised in the 1960s with the release of Pressline sheets containing Lorem Ipsum passages, and more recently with desktop publishing software like Folio LayoutDesk including versions of Lorem Ipsum.</p>
  </section>

  <footer class="site-footer">
    <nav class="footer-nav">
      <a href="#">Home</a>
      <a href="#">About Us</a>
      <a href="#">Terms and Conditions</a>
      <a href="#">Privacy Policy</a>
      <a href="#">Orvane Store</a>
      <a href="#">Contact Us</a>
    </nav>
    <div class="copyright">Tulvo Pty Ltd 2014</div>
    <div class="footer-social">
      <span class="social-dot" role="img" aria-label="Social network link"></span>
      <span class="social-dot" role="img" aria-label="Social network link"></span>
      <span class="social-dot" role="img" aria-label="Social network link"></span>
    </div>
  </footer>
</body>
</html>
```